CANNABIS GROWING MACHINES Business Card Design

I created a front and back idea of what I want. Also I included my Brightleaf Plot logo to be used on the card. Please use your creativity to make it look professional and awesome! Use the all text and phrases in the sample card that I made.

(Front of card)Key words and phrases:
CANNABIS GROWING MACHINES
Aeroponics Technology
No soil
No pesticides
98% less water
Grow year round

(Back of card)
EVERY MONTH ONE SPIRE PLANTER WILL BE GIVEN AWAY
FOLLOW US ON IG FOR A CHANCE TO WIN A SPIRE PLANTER
CANNABIS GROWING MACHINES
Vertical Farming
Urban Farming
100% Organic
Grows 40% Faster
Indoors/outdoors

My contact info:
Chef Rom
Phone:555 014-3397
web: brightleafplot.example
IG: mossyfingerscrew

Target Market(s)

Cannabis Cultivation, Gardening, Urban farming, Vertical farming

Industry/Entity Type

Cannabis

Contact Information for Business Card

My contact info:
Chef Rom
Phone:555 014-3397
web: brightleafplot.example
IG: mossyfingerscrew

Requirements
Must have
• My contact info:
Chef Rom
Phone:555 014-3397
web: brightleafplot.example
IG: mossyfingerscrew
Nice to have
• Awesome Cannabis imagery throughout the card front and back.

```html
<!DOCTYPE html>
<html lang="en">
<head>
<meta charset="UTF-8">
<title>Brightleaf Plot – Business Card</title>
<link rel="stylesheet" href="https://fonts.googleapis.com/css2?family=Montserrat:wght@500;600;700;800&family=Oswald:wght@700&display=swap">
<style>
  :root {
    --page-bg: #e6e3df;
    --lime: #8cc63f;
    --lime-bright: #9fdc2a;
    --pink: #e8285f;
    --ink: #0c1118;
    --white: #ffffff;
    --photo-dark: #2b2f2a;
    --photo-mid: #3d4a37;
  }
  * { margin: 0; padding: 0; box-sizing: border-box; }
  html, body {
    width: 1200px; height: 1110px; overflow: hidden;
    background: var(--page-bg);
    font-family: "Montserrat", sans-serif;
  }
  .card {
    position: absolute; left: 150px; width: 900px; height: 514px;
    overflow: hidden; box-shadow: 0 6px 18px rgba(0,0,0,.18);
  }

  /* Promo side */
  .card--promo { top: 30px; background: var(--photo-dark); }
  .promo__band {
    position: absolute; left: 0; right: 0; height: 48px;
    display: flex; align-items: center; justify-content: center;
    color: var(--white); font-weight: 600; font-size: 17px; letter-spacing: .06em;
  }
  .promo__band--top { top: 0; background: var(--lime); }
  .promo__band--bottom { bottom: 0; background: var(--pink); }
  .promo__photo {
    position: absolute; top: 48px; bottom: 48px; left: 0; right: 0;
    background: linear-gradient(160deg, #4a5546 0%, var(--photo-mid) 35%, var(--photo-dark) 75%, #1f231e 100%);
  }
  .promo__heading {
    position: absolute; top: 100px; left: 0; right: 0; text-align: center;
    font-family: "Oswald", sans-serif; font-weight: 700;
    font-size: 44px; letter-spacing: .04em; color: var(--lime-bright);
  }
  .promo__lists {
    position: absolute; top: 190px; left: 0; right: 0;
    display: flex; justify-content: center; gap: 40px;
  }
  .feature-list { list-style: none; display: flex; flex-direction: column; gap: 16px; }
  .feature-list li {
    display: flex; align-items: center; gap: 16px;
    color: var(--white); font-weight: 500; font-size: 21px; letter-spacing: .03em;
  }
  .feature-list--left li { justify-content: flex-end; }
  .tick { width: 24px; height: 20px; flex: none; }

  /* Contact side */
  .card--contact { top: 566px; background: var(--ink); }
  .contact__name {
    position: absolute; left: 70px; top: 230px;
    color: var(--pink); font-weight: 800; font-size: 58px; letter-spacing: .01em;
  }
  .contact__list { position: absolute; left: 74px; top: 318px; list-style: none; display: flex; flex-direction: column; gap: 12px; }
  .contact__list li { display: flex; align-items: center; gap: 18px; color: var(--white); font-weight: 500; font-size: 21px; }
  .contact__icon { width: 22px; height: 22px; flex: none; }
  .contact__leaf {
    position: absolute; left: 400px; top: 150px; width: 230px; height: 230px; border-radius: 50%;
    background: radial-gradient(circle, #6fd12a 0%, #2f8a16 35%, rgba(20,80,10,.45) 58%, rgba(12,17,24,0) 72%);
  }
  .contact__brand {
    position: absolute; left: 655px; top: 170px; display: flex; align-items: center; gap: 12px;
  }
  .contact__brand-name {
    color: var(--lime-bright); font-weight: 800; font-size: 34px; line-height: 1.02; letter-spacing: .02em;
  }
  .contact__brand-dot { width: 22px; height: 22px; border-radius: 50%; background: var(--lime-bright); flex: none; }
</style>
</head>
<body>

<section class="card card--promo">
  <div class="promo__photo" role="img" aria-label="Greenhouse full of young cannabis plants, darkened"></div>
  <div class="promo__band promo__band--top">EVERY MONTH ONE SPIRE PLANTER WILL BE GIVEN AWAY</div>
  <h2 class="promo__heading">CANNABIS GROWING MACHINES</h2>
  <div class="promo__lists">
    <ul class="feature-list feature-list--left">
      <li>Aeroponics Technology<svg class="tick" viewBox="0 0 24 20"><path d="M2 10l7 7L22 3" fill="none" stroke="#9fdc2a" stroke-width="4" stroke-linecap="round" stroke-linejoin="round"/></svg></li>
      <li>No soil<svg class="tick" viewBox="0 0 24 20"><path d="M2 10l7 7L22 3" fill="none" stroke="#9fdc2a" stroke-width="4" stroke-linecap="round" stroke-linejoin="round"/></svg></li>
      <li>No pesticides<svg class="tick" viewBox="0 0 24 20"><path d="M2 10l7 7L22 3" fill="none" stroke="#9fdc2a" stroke-width="4" stroke-linecap="round" stroke-linejoin="round"/></svg></li>
      <li>98% less water<svg class="tick" viewBox="0 0 24 20"><path d="M2 10l7 7L22 3" fill="none" stroke="#9fdc2a" stroke-width="4" stroke-linecap="round" stroke-linejoin="round"/></svg></li>
      <li>Grow year round<svg class="tick" viewBox="0 0 24 20"><path d="M2 10l7 7L22 3" fill="none" stroke="#9fdc2a" stroke-width="4" stroke-linecap="round" stroke-linejoin="round"/></svg></li>
    </ul>
    <ul class="feature-list feature-list--right">
      <li><svg class="tick" viewBox="0 0 24 20"><path d="M2 10l7 7L22 3" fill="none" stroke="#9fdc2a" stroke-width="4" stroke-linecap="round" stroke-linejoin="round"/></svg>Vertical Farming</li>
      <li><svg class="tick" viewBox="0 0 24 20"><path d="M2 10l7 7L22 3" fill="none" stroke="#9fdc2a" stroke-width="4" stroke-linecap="round" stroke-linejoin="round"/></svg>Urban Farming</li>
      <li><svg class="tick" viewBox="0 0 24 20"><path d="M2 10l7 7L22 3" fill="none" stroke="#9fdc2a" stroke-width="4" stroke-linecap="round" stroke-linejoin="round"/></svg>100% Organic</li>
      <li><svg class="tick" viewBox="0 0 24 20"><path d="M2 10l7 7L22 3" fill="none" stroke="#9fdc2a" stroke-width="4" stroke-linecap="round" stroke-linejoin="round"/></svg>Grows 40% Faster</li>
      <li><svg class="tick" viewBox="0 0 24 20"><path d="M2 10l7 7L22 3" fill="none" stroke="#9fdc2a" stroke-width="4" stroke-linecap="round" stroke-linejoin="round"/></svg>Indoors/outdoors</li>
    </ul>
  </div>
  <div class="promo__band promo__band--bottom">FOLLOW US ON IG FOR A CHANCE TO WIN A SPIRE PLANTER</div>
</section>

<section class="card card--contact">
  <div class="contact__leaf" role="img" aria-label="Glowing green cannabis leaf illustration"></div>
  <div class="contact__brand">
    <span class="contact__brand-name">BRIGHTLEAF<br>PLOT</span>
    <span class="contact__brand-dot"></span>
  </div>
  <h1 class="contact__name">Chef Rom</h1>
  <ul class="contact__list">
    <li>
      <svg class="contact__icon" viewBox="0 0 24 24"><path d="M6.6 10.8a15 15 0 006.6 6.6l2.2-2.2a1 1 0 011-.25 11.4 11.4 0 003.6.6 1 1 0 011 1V20a1 1 0 01-1 1A17 17 0 013 4a1 1 0 011-1h3.5a1 1 0 011 1c0 1.25.2 2.45.6 3.6a1 1 0 01-.25 1z" fill="#e8285f"/></svg>
      555 014-3397
    </li>
    <li>
      <svg class="contact__icon" viewBox="0 0 24 24"><g fill="none" stroke="#e8285f" stroke-width="2"><circle cx="12" cy="12" r="9.5"/><path d="M2.5 12h19M12 2.5c3 3 3 16 0 19M12 2.5c-3 3-3 16 0 19"/></g></svg>
      www.brightleafplot.example
    </li>
    <li>
      <svg class="contact__icon" viewBox="0 0 24 24"><rect x="4" y="4" width="16" height="16" fill="#e8285f"/></svg>
      mossyfingerscrew
    </li>
  </ul>
</section>

</body>
</html>
```